Jewelery Website

Please visit: http://www.kelidunmore.example/dev/wpnew/

Target Market(s)

Women between 25 and 44 years old

Number of Pages Required

5+ page

Font styles to use
Sans Serif
Script
Other font styles liked:
• Futura

Colors

Designer to choose colors to be used in the design.

```html
<!DOCTYPE html>
<html lang="en">
<head>
<meta charset="utf-8">
<title>Keli Dunmore Pearls — Jewellery Store</title>
<link href="https://fonts.googleapis.com/css2?family=Montserrat:wght@300;400;600;700&family=Lato:wght@400;700&display=swap" rel="stylesheet">
<style>
:root{
  --backdrop:#d8d8d8;
  --page:#ffffff;
  --ink:#1a1a1a;
  --muted:#777777;
  --line:#e2e2e2;
  --soft:#f4f4f4;
  --dark:#0d0f12;
  --footer:#1c1c1c;
  --accent:#d7263d;
  --gold:#b98a3c;
}
*{box-sizing:border-box;margin:0;padding:0}
html,body{width:960px;height:1200px;overflow:hidden}
body{background:var(--backdrop);font-family:"Lato",sans-serif;color:var(--ink)}
.page{position:absolute;left:181px;top:0;width:569px;height:1200px;background:var(--page);overflow:hidden}
.abs{position:absolute}
/* top bar */
.topbar{left:0;top:0;width:569px;height:30px;background:#f6f6f4;border-bottom:1px solid var(--line)}
.topbar .contact{left:50px;top:10px;font-size:5.4px;color:#333;white-space:nowrap}
.brand-box{left:258px;top:0;width:35px;height:30px;background:#1b1b1b;display:flex;align-items:center;justify-content:center;overflow:hidden}
.brand-box span{font-family:"Montserrat",sans-serif;font-weight:600;color:#fff;font-size:4.6px;letter-spacing:.2px;white-space:nowrap}
.toplinks{top:11px;font-size:5px;color:#333;white-space:nowrap}
/* nav */
.nav{left:0;top:30px;width:569px;height:17px;background:#f6f6f4}
.nav .home{left:51px;top:0;width:17px;height:17px;background:var(--accent)}
.nav .item{top:5px;font-size:5.4px;color:#222;white-space:nowrap}
.tag{font-size:3.6px;background:var(--accent);color:#fff;padding:0 2px;position:absolute;top:-5px;border-radius:1px;white-space:nowrap}
/* hero */
.hero{left:0;top:47px;width:569px;height:213px;background:linear-gradient(90deg,#1d2a33 0%,#17232c 40%,#0b0e12 70%,#080a0c 100%)}
.hero .art{left:0;top:0;width:260px;height:213px;background:radial-gradient(ellipse at 45% 55%,#8a6a2c 0%,#4a3a1f 30%,#1c2a33 65%,transparent 100%)}
.hero h1{left:297px;top:76px;width:280px;text-align:center;font-family:"Montserrat",sans-serif;font-weight:400;color:#fff;font-size:19px;line-height:25px;letter-spacing:.3px;white-space:nowrap}
.hero p{left:307px;top:134px;width:260px;text-align:center;color:#fff;font-size:6px;line-height:10px;font-family:"Montserrat",sans-serif;white-space:nowrap}
/* promo tiles */
.tile{background:var(--dark);border:1px solid #222;overflow:hidden}
.tile::after{content:"";position:absolute;inset:4px;border:1px solid #5a5a5a;z-index:3;pointer-events:none}
.btn-ghost{position:absolute;border:1px solid #ddd;color:#fff;font-size:6.4px;text-align:center;line-height:13px;font-family:"Montserrat",sans-serif;z-index:2}
.tile .t{position:absolute;color:#fff;font-family:"Montserrat",sans-serif;z-index:2;white-space:nowrap}
.art-fill{position:absolute;z-index:1}
/* section titles */
.sec-title{width:569px;left:0;text-align:center;font-family:"Montserrat",sans-serif;font-weight:700;font-size:11px;letter-spacing:.5px}
.sec-rule{height:1px;background:var(--line)}
/* products */
.card{top:470px;width:115px;height:137px;border:1px solid #eee;background:#fff;text-align:center}
.card .img{position:absolute;left:16px;top:10px;width:82px;height:86px;border-radius:50%}
.card .name{position:absolute;left:0;width:100%;top:105px;font-size:5.4px;color:#444;font-family:"Montserrat",sans-serif}
.card .price{position:absolute;left:0;width:100%;top:114px;font-size:8px;font-style:italic;color:#222}
.card .stars{position:absolute;left:0;width:100%;top:125px;font-size:6px;color:#c8c8c8;letter-spacing:.5px}
/* features */
.features{left:0;top:779px;width:569px;height:85px;background:var(--soft)}
.feat{top:0;width:170px;height:85px;text-align:center}
.feat svg{position:absolute;left:77px;top:13px}
.feat h3{position:absolute;width:100%;top:44px;font-size:7.4px;font-family:"Montserrat",sans-serif;font-weight:600}
.feat p{position:absolute;width:100%;top:56px;font-size:5px;color:var(--muted)}
.vdiv{top:10px;width:1px;height:68px;background:#d6d6d6}
/* partners */
.pbtn{top:935px;width:22px;height:14px;border:1px solid #ccc;background:#eee;font-size:5.4px;line-height:12px;text-align:center;color:#555}
.badge{top:934px;width:58px;height:16px;border-radius:8px;background:#ececec}
/* newsletter */
.newsletter{left:0;top:978px;width:569px;height:100px;background:var(--soft)}
.nl-label{left:44px;top:1042px;font-size:7px;font-weight:700;white-space:nowrap}
.nl-input{top:1037px;height:19px;background:#fff;border:1px solid #ccc;font-size:5px;color:#999;padding-left:6px;line-height:17px}
.nl-submit{left:454px;top:1037px;width:62px;height:19px;background:#1c1c1c;color:#fff;font-size:5.4px;font-weight:700;text-align:center;line-height:19px;font-family:"Montserrat",sans-serif}
/* footer */
.footer{left:0;top:1078px;width:569px;height:122px;background:var(--footer)}
.foot-logo{left:40px;top:1085px;width:89px;height:75px;border:1px solid #777;display:flex;align-items:center;justify-content:center}
.foot-logo::after{content:"";position:absolute;inset:3px;border:1px solid #555}
.foot-logo span{font-family:"Montserrat",sans-serif;font-weight:600;color:#fff;font-size:10px;letter-spacing:1px;text-align:center;line-height:13px}
.social{top:1172px;width:12px;height:12px;background:#444}
.fcol h4{font-family:"Montserrat",sans-serif;font-weight:600;color:#fff;font-size:7px;position:absolute;top:0;white-space:nowrap}
.fcol ul{list-style:none;position:absolute;top:23px}
.fcol li{font-size:5.2px;color:#999;line-height:10.3px;white-space:nowrap}
.fcol li::before{content:"•";margin-right:4px;color:#999}
.fcol p{font-size:5.2px;color:#999;position:absolute;white-space:nowrap}
</style>
</head>
<body>
<div class="page">

  <header>
    <div class="abs topbar">
      <div class="abs contact">Contact us on 123 456 7890 or info@kelidunmore.example</div>
      <div class="abs brand-box"><span>DUNMORE</span></div>
      <div class="abs toplinks" style="left:418px">$ Currency ⌄</div>
      <div class="abs toplinks" style="left:455px">My Account ⌄</div>
      <div class="abs toplinks" style="left:501px">Checkout</div>
    </div>
    <nav class="abs nav">
      <div class="abs home">
        <svg width="17" height="17" viewBox="0 0 17 17"><path d="M5.5 9 L8.5 6 L11.5 9 V11.5 H5.5Z" fill="#fff"/></svg>
      </div>
      <div class="abs item" style="left:75px">Gold Jewelery ▾</div>
      <div class="abs item" style="left:133px">Diamond ▾<span class="tag" style="left:29px">Hot</span></div>
      <div class="abs item" style="left:186px">Women ▾</div>
      <div class="abs item" style="left:227px">Our Products ▾<span class="tag" style="left:45px">New</span></div>
      <div class="abs item" style="left:290px">Pages ▾</div>
      <div class="abs item" style="left:325px">Buy this theme ▾<span class="tag" style="left:48px">Click here</span></div>
      <svg class="abs" style="left:437px;top:5px" width="7" height="7" viewBox="0 0 7 7"><circle cx="3" cy="3" r="2.2" fill="none" stroke="#222" stroke-width="1"/><path d="M4.6 4.6 L6.5 6.5" stroke="#222" stroke-width="1"/></svg>
      <svg class="abs" style="left:452px;top:5px" width="7" height="7" viewBox="0 0 10 10"><path d="M5 9 L1 5 A2.3 2.3 0 0 1 5 2 A2.3 2.3 0 0 1 9 5Z" fill="#222"/></svg>
      <svg class="abs" style="left:466px;top:5px" width="7" height="7" viewBox="0 0 10 10"><path d="M2 3 H8 L7.5 9 H2.5Z M3.5 3 V2 A1.5 1.5 0 0 1 6.5 2 V3" fill="#222" stroke="#222" stroke-width=".6"/></svg>
      <div class="abs item" style="left:477px">0 item(s) - $0.00</div>
    </nav>
  </header>

  <section class="abs hero">
    <div class="abs art" role="img" aria-label="Gold kundan necklace with red silk cord on a dark blue textured backdrop"></div>
    <h1 class="abs">MINIMAL<br>STOREFRONT THEME</h1>
    <p class="abs">'60s-inspired bangles, pendants, and head pieces<br>from Mara Ellison's boho-chic line</p>
  </section>

  <section class="promos">
    <div class="abs tile" style="left:40px;top:275px;width:152px;height:152px">
      <div class="art-fill" role="img" aria-label="Pair of diamond engagement rings" style="left:26px;top:12px;width:100px;height:68px;background:radial-gradient(ellipse,#9a9a9a 0%,#3a3a3a 50%,transparent 75%)"></div>
      <div class="t" style="left:0;width:152px;text-align:center;top:87px;font-size:6.2px;letter-spacing:.4px">EXCLUSIVE OFFER</div>
      <div class="t" style="left:0;width:152px;text-align:center;top:96px;font-size:10px;letter-spacing:.5px">DIAMOND COLLECTION</div>
      <div class="btn-ghost" style="left:42px;top:116px;width:68px;height:15px">Shop Now!</div>
    </div>
    <div class="abs tile" style="left:210px;top:275px;width:316px;height:152px">
      <div class="art-fill" role="img" aria-label="Gold bridal necklace and earrings set on dark fabric" style="left:150px;top:18px;width:160px;height:120px;background:radial-gradient(ellipse at 45% 50%,#a07a30 0%,#4a3818 35%,#1a1a1a 65%,transparent 80%)"></div>
      <div class="t" style="left:14px;width:150px;text-align:center;top:30px;font-size:14px;font-weight:300;line-height:18px">Wedding Jewellery<br>Collection</div>
      <div style="position:absolute;left:72px;top:78px;width:34px;height:1px;background:#aaa;z-index:2"></div>
      <div class="btn-ghost" style="left:43px;top:99px;width:69px;height:15px">Shop Now!</div>
    </div>
  </section>

  <section class="latest">
    <h2 class="abs sec-title" style="top:437px">LATEST</h2>
    <div class="abs sec-rule" style="left:240px;top:458px;width:88px"></div>
    <article class="abs card" style="left:42px">
      <div class="img" role="img" aria-label="Gold ring with diamond band" style="background:radial-gradient(circle,#e8c877 0%,#f5ecd5 55%,#fff 75%)"></div>
      <div class="name">VOLUTRAP EART</div><div class="price">$123.20</div><div class="stars">★★★★★</div>
    </article>
    <article class="abs card" style="left:166px">
      <div class="img" role="img" aria-label="Gold cocktail ring set with diamonds" style="background:radial-gradient(circle,#dcb558 0%,#f3e6c4 55%,#fff 75%)"></div>
      <div class="name">VOLUTRAP EART</div><div class="price">$123.20</div><div class="stars">★★★★★</div>
    </article>
    <article class="abs card" style="left:290px">
      <div class="img" role="img" aria-label="Stacked silver and gold bands" style="background:radial-gradient(circle,#a8a8a8 0%,#e6e6e6 55%,#fff 75%)"></div>
      <div class="name">VOLUTRAP EART</div><div class="price">$123.20</div><div class="stars">★★★★★</div>
    </article>
    <article class="abs card" style="left:413px">
      <div class="img" role="img" aria-label="Open-work gold ring with diamonds" style="background:radial-gradient(circle,#e0bd66 0%,#f5ead0 55%,#fff 75%)"></div>
      <div class="name">VOLUTRAP EART</div><div class="price">$123.20</div><div class="stars">★★★★★</div>
    </article>
  </section>

  <section class="promos-2">
    <div class="abs tile" style="left:41px;top:627px;width:234px;height:143px">
      <div class="art-fill" role="img" aria-label="Pair of ornate gold bangles" style="left:110px;top:20px;width:118px;height:100px;background:radial-gradient(ellipse,#c8962e 0%,#6a4a14 40%,#111 70%,transparent 85%)"></div>
      <div class="t" style="left:10px;top:37px;font-size:7.4px;letter-spacing:.6px">EXCLUSIVE</div>
      <div class="t" style="left:10px;top:48px;font-size:15px;line-height:19px;letter-spacing:.6px">GOLD<br>JEWELLERY</div>
      <div class="btn-ghost" style="left:10px;top:94px;width:68px;height:15px">Shop Now!</div>
    </div>
    <div class="abs tile" style="left:294px;top:627px;width:233px;height:143px">
      <div class="art-fill" role="img" aria-label="Model wearing a statement silver necklace" style="left:110px;top:0;width:121px;height:141px;background:linear-gradient(90deg,#0d0f12 0%,#5a4036 45%,#c9a08a 75%,#7a5a4c 100%)"></div>
      <div class="t" style="left:13px;top:37px;font-size:14px;line-height:17px;letter-spacing:.5px">IMITATION<br><span style="font-weight:300">JEWELLERY<br>COLLECTION</span></div>
      <div class="btn-ghost" style="left:13px;top:94px;width:68px;height:15px">Shop Now!</div>
    </div>
  </section>

  <section class="abs features">
    <div class="abs feat" style="left:30px">
      <svg width="16" height="20" viewBox="0 0 16 20"><path d="M8 19 C3 12 1.5 9.5 1.5 7 A6.5 6.5 0 0 1 14.5 7 C14.5 9.5 13 12 8 19Z" fill="none" stroke="#888" stroke-width="1"/><circle cx="8" cy="7" r="2.2" fill="none" stroke="#888"/></svg>
      <h3>FREE SHIPPING</h3><p>In Order Min. $200</p>
    </div>
    <div class="abs vdiv" style="left:200px"></div>
    <div class="abs feat" style="left:200px">
      <svg width="20" height="20" viewBox="0 0 20 20"><circle cx="10" cy="10" r="8.5" fill="none" stroke="#888"/><text x="10" y="14" text-anchor="middle" font-size="11" fill="#888" font-family="Lato,sans-serif">$</text></svg>
      <h3>MONEY BACK</h3><p>100% Money Back in 30 days</p>
    </div>
    <div class="abs vdiv" style="left:369px"></div>
    <div class="abs feat" style="left:369px">
      <svg width="20" height="18" viewBox="0 0 20 18"><path d="M10 2 C15 2 18.5 4.8 18.5 8 C18.5 11.2 15 14 10 14 C8.8 14 7.8 13.8 6.8 13.5 L2.5 16 L3.8 12 C2.3 11 1.5 9.6 1.5 8 C1.5 4.8 5 2 10 2Z" fill="none" stroke="#888"/></svg>
      <h3>24 H SUPPORT</h3><p>Service support fast 24/7</p>
    </div>
  </section>

  <section class="partners">
    <h2 class="abs sec-title" style="top:882px">OUR PARTNER</h2>
    <div class="abs sec-rule" style="left:38px;top:902px;width:493px"></div>
    <div class="abs pbtn" style="left:39px">Prev</div>
    <div class="abs badge" style="left:76px"></div>
    <div class="abs badge" style="left:162px"></div>
    <div class="abs badge" style="left:248px"></div>
    <div class="abs badge" style="left:334px"></div>
    <div class="abs badge" style="left:420px"></div>
    <div class="abs pbtn" style="left:507px">Next</div>
  </section>

  <section class="abs newsletter"></section>
  <h2 class="abs sec-title" style="top:995px">NEWSLETTER</h2>
  <div class="abs sec-rule" style="left:240px;top:1016px;width:88px;background:#d6d6d6"></div>
  <div class="abs nl-label">Subscribe to us</div>
  <div class="abs nl-input" style="left:106px;width:169px">Enter Your Name</div>
  <div class="abs nl-input" style="left:280px;width:169px">Enter Your Email</div>
  <div class="abs nl-submit">SUBMIT</div>

  <footer class="abs footer"></footer>
  <div class="abs foot-logo"><span>KELI<br>DUNMORE</span></div>
  <div class="abs social" style="left:45px"></div>
  <div class="abs social" style="left:63px"></div>
  <div class="abs social" style="left:81px"></div>
  <div class="abs social" style="left:99px"></div>
  <div class="abs social" style="left:117px"></div>

  <div class="abs fcol" style="left:167px;top:1102px">
    <h4>MY ACCOUNT</h4>
    <ul><li>My Account</li><li>Order History</li><li>Wish List</li><li>Newsletter</li></ul>
  </div>
  <div class="abs fcol" style="left:290px;top:1102px">
    <h4>INFORMATION</h4>
    <ul><li>About Us</li><li>Delivery Information</li><li>Privacy Policy</li><li>Terms &amp; Conditions</li></ul>
  </div>
  <div class="abs fcol" style="left:414px;top:1102px">
    <h4>CONTACT US</h4>
    <p style="top:23px;line-height:8px">Lorem ipsum dolor sit amet, consectetur<br>adipiscing elit.</p>
    <p style="top:44px">➤&nbsp; 123, Lorem Ipsum, India</p>
    <p style="top:54px">✉&nbsp; info@kelidunmore.example</p>
    <p style="top:63px">☏&nbsp; 123 456 7890</p>
  </div>

</div>
</body>
</html>
```